Mina Vell makeup artist business cards

Hello
I need business cards for my freelance makeup artist business.

What I am looking for;
Sleek
Clear and easily read
Expensive/exclusive feel
Black and white
Embossed

Information that must be included on back
My name
My contact number
My email
My website
My Facebook
My Instagram

If it works I'd like to also include on the back;
Bridal, glamour, evening, editorial, fashion, tv, film makeup
(Open to exclude if it makes the card look to busy)

Requirements
Must have
• My logo mina Vell makeup artist as shown in photos
Nice to have
• I'd like to see some designs with the social media icons (as shown in image attached)

```html
<!DOCTYPE html>
<html lang="en">
<head>
<meta charset="utf-8">
<title>Mina Vell — Makeup Artist Business Card</title>
<link rel="stylesheet" href="https://fonts.googleapis.com/css2?family=Josefin+Sans:wght@300&family=Share+Tech+Mono&display=swap">
<style>
  :root {
    --canvas: #050707;
    --card-front: #f4f6f8;
    --ink-dark: #2f3436;
    --ink-light: #f2f2f2;
    --accent-band: #0a2aa8;
    --divider: #d9d9d9;
  }
  * { margin: 0; padding: 0; box-sizing: border-box; }
  html, body {
    width: 1009px; height: 1200px; overflow: hidden;
    background: var(--canvas);
  }
  .canvas { position: relative; width: 1009px; height: 1200px; background: var(--canvas); }

  .card-front {
    position: absolute; left: 10px; top: 11px; width: 988px; height: 567px;
    background: var(--card-front);
  }
  .brand-mark {
    position: absolute; left: 410px; top: 121px; width: 176px; height: 176px;
    border-radius: 50%; background: var(--ink-dark);
  }
  .wordmark {
    position: absolute; left: 0; width: 100%; text-align: center;
    font-family: "Josefin Sans", sans-serif; font-weight: 300; color: var(--ink-dark);
    text-transform: uppercase; white-space: nowrap;
  }
  .card-front .brand-name { top: 362px; font-size: 46px; letter-spacing: 0.55em; padding-left: 0.55em; }
  .card-front .brand-role { top: 428px; font-size: 18px; letter-spacing: 1.15em; padding-left: 1.15em; }

  .accent-band {
    position: absolute; left: 0; top: 590px; width: 1009px; height: 20px;
    background: var(--accent-band);
  }

  .card-back { position: absolute; left: 0; top: 610px; width: 1009px; height: 590px; }
  .back-identity { position: absolute; left: 84px; top: 240px; width: 330px; color: var(--ink-light); }
  .back-identity .brand-name {
    font-family: "Josefin Sans", sans-serif; font-weight: 300;
    font-size: 31px; letter-spacing: 0.5em; text-transform: uppercase; white-space: nowrap;
  }
  .back-identity .brand-role {
    font-family: "Josefin Sans", sans-serif; font-weight: 300;
    font-size: 12px; letter-spacing: 1.05em; text-transform: uppercase; white-space: nowrap;
    margin-top: 2px;
  }
  .name-field {
    font-family: "Share Tech Mono", monospace; font-size: 36px; letter-spacing: 0.12em;
    margin-top: 2px; white-space: nowrap;
  }
  .divider {
    position: absolute; left: 492px; top: 92px; width: 2px; height: 445px;
    background: var(--divider);
  }
  .contact-icons { position: absolute; left: 516px; top: 162px; list-style: none; }
  .contact-icons li { width: 48px; height: 48px; margin-bottom: 23.5px; }
  .contact-icons svg { display: block; width: 48px; height: 48px; }
</style>
</head>
<body>
<main class="canvas">
  <section class="card-front">
    <div class="brand-mark"></div>
    <div class="wordmark brand-name">Mina Vell</div>
    <div class="wordmark brand-role">Makeup&nbsp;&nbsp;Artist</div>
  </section>

  <div class="accent-band"></div>

  <section class="card-back">
    <div class="back-identity">
      <div class="brand-name">Mina Vell</div>
      <div class="brand-role">Makeup&nbsp;&nbsp;Artist</div>
      <div class="name-field">NAME----------</div>
    </div>

    <div class="divider"></div>

    <ul class="contact-icons">
      <li class="icon-phone">
        <svg viewBox="0 0 48 48" aria-label="Phone">
          <circle cx="24" cy="24" r="23" fill="#fff"/>
          <path d="M12 19 q12 -8 24 0 v3 h-6 v-3 q-6 -2 -12 0 v3 h-6 z" fill="#111"/>
          <rect x="16" y="23" width="16" height="11" rx="1.5" fill="#111"/>
          <g fill="#fff"><rect x="19" y="25.5" width="2" height="2"/><rect x="23" y="25.5" width="2" height="2"/><rect x="27" y="25.5" width="2" height="2"/><rect x="19" y="29.5" width="2" height="2"/><rect x="23" y="29.5" width="2" height="2"/><rect x="27" y="29.5" width="2" height="2"/></g>
        </svg>
      </li>
      <li class="icon-web">
        <svg viewBox="0 0 48 48" aria-label="Website">
          <circle cx="24" cy="24" r="23" fill="#fff"/>
          <circle cx="24" cy="24" r="14" fill="#111"/>
          <g fill="none" stroke="#fff" stroke-width="1.4">
            <ellipse cx="24" cy="24" rx="6" ry="14"/>
            <line x1="10" y1="24" x2="38" y2="24"/>
            <path d="M13 17 h22 M13 31 h22"/>
          </g>
        </svg>
      </li>
      <li class="icon-email">
        <svg viewBox="0 0 48 48" aria-label="Email">
          <circle cx="24" cy="24" r="23" fill="#fff"/>
          <rect x="11" y="15" width="26" height="18" fill="none" stroke="#111" stroke-width="2"/>
          <polyline points="11,15 24,26 37,15" fill="none" stroke="#111" stroke-width="2"/>
          <path d="M11 33 l10 -9 M37 33 l-10 -9" stroke="#111" stroke-width="1.5"/>
        </svg>
      </li>
      <li class="icon-social">
        <svg viewBox="0 0 48 48" aria-label="Social profile">
          <circle cx="24" cy="24" r="23" fill="#fff"/>
        </svg>
      </li>
      <li class="icon-social">
        <svg viewBox="0 0 48 48" aria-label="Social profile">
          <circle cx="24" cy="24" r="23" fill="#fff"/>
        </svg>
      </li>
    </ul>
  </section>
</main>
</body>
</html>
```